Brookvale Systems Yellow rose letterhead

I have a new logo for my company but in its current form it is too large to be used on letterhead or as a email signature. I need to have the designer use elements from the current logo and create something close to the original but more suited for smaller items.
Updates

I just uploaded a copy of our logo that does not have the weathered affect. Thanks

Industry/Entity Type

It Company

Requirements
Must have
• The design must maintain the visual effect of the current logo. It needs to include the yellow rose and the name of the company.
Nice to have
• It would be nice to maintain the stamp theme and incorporate my name, address, phone, email. etc.

```html
<!DOCTYPE html>
<html lang="en">
<head>
<meta charset="utf-8">
<title>Brookvale Systems Stationery</title>
<link href="https://fonts.googleapis.com/css2?family=Open+Sans:ital,wght@0,400;0,700;1,400&family=Nothing+You+Could+Do&display=swap" rel="stylesheet">
<style>
:root{
  --bg:#ececec;
  --paper:#ffffff;
  --brown:#4b3d37;
  --gold:#f2c12e;
  --gold-deep:#e2a816;
  --ink:#444;
  --muted:#8a8a8a;
}
*{margin:0;padding:0;box-sizing:border-box}
html,body{width:1200px;height:900px;overflow:hidden;background:var(--bg);font-family:"Open Sans",sans-serif;color:var(--ink)}
.canvas{position:relative;width:1200px;height:900px}

/* brand mark */
.brand{display:flex;align-items:center;gap:5px}
.brand-square{width:12px;height:12px;background:var(--gold);flex:none}
.brand-name{font-family:"Open Sans",sans-serif;font-weight:700;font-size:12px;line-height:1.1;color:var(--brown)}

/* letterhead */
.letterhead{position:absolute;left:86px;top:110px;width:504px;height:680px;background:var(--paper);overflow:hidden}
.lh-brand{position:absolute;left:14px;top:30px;width:88px}
.lh-rule{position:absolute;left:104px;top:10px;width:1px;height:110px;background:var(--gold)}
.contact{position:absolute;font-style:italic;font-weight:400;font-size:8px;line-height:10px;color:var(--muted)}
.contact .person{font-size:10px;color:#666}
.lh-contact{left:117px;top:16px}
.lh-swoosh{position:absolute;right:8px;top:12px}
.lh-band{position:absolute;left:0;top:95px;width:504px;height:25px;background:var(--brown);border-top:2px solid var(--gold)}
.lh-band p{position:absolute;left:116px;top:6px;font-size:7.5px;font-weight:700;color:#fff;white-space:nowrap}
.recipient{position:absolute;left:115px;top:162px;font-style:italic;font-size:7px;line-height:11px;color:#555}
.letter{position:absolute;left:115px;top:226px;width:290px;font-size:6.4px;line-height:9.6px;color:#666;text-align:justify}
.letter p{margin-bottom:9px}
.signoff{position:absolute;left:115px;top:490px;font-size:7px;color:#666}
.signature{position:absolute;left:115px;top:505px;font-family:"Nothing You Could Do",cursive;font-size:19px;color:#666}
.initials{position:absolute;left:115px;top:540px;font-size:6.5px;color:#666}
.lh-footer{position:absolute;left:0;top:0}
.rose-art{position:absolute;left:345px;top:528px;width:159px;height:152px;border-radius:60% 0 0 0;background:radial-gradient(circle at 55% 50%,#fbe26a 0%,#f5c92c 45%,#e4a818 100%)}

/* envelopes */
.envelope{position:absolute;left:638px;width:537px;background:var(--paper)}
.env-back{top:125px;height:255px}
.env-flap{position:absolute;left:0;top:0;width:537px;height:90px;background:var(--brown)}
.env-flap-line{position:absolute;left:0;top:58px;width:537px;height:2px;background:var(--gold)}
.env-flap-brand{position:absolute;left:226px;top:22px;width:82px;height:52px;background:var(--brown);border:2px solid var(--gold);padding:6px;display:flex;align-items:center}
.env-flap-brand .brand-name{color:#fff;font-size:11px}

.env-front{top:467px;height:263px}
.env-stripes{position:absolute;left:0;top:0;width:537px}
.stripe-brown{height:12px;background:var(--brown)}
.stripe-gold{height:2px;background:var(--gold);margin-top:5px}
.stripe-grey{height:2px;background:#c9c9c9;margin-top:2px}
.env-brand{position:absolute;left:30px;top:50px;width:88px}
.env-rule{position:absolute;left:122px;top:30px;width:1px;height:70px;background:var(--gold)}
.env-contact{left:132px;top:36px}
.env-tagline{position:absolute;left:130px;top:233px;display:flex;align-items:center;gap:12px;font-size:9px;color:#555;white-space:nowrap}
.env-tagline .divider{width:1px;height:12px;background:var(--gold)}
.env-tagline em{color:var(--muted)}
</style>
</head>
<body>
<main class="canvas">

  <section class="letterhead">
    <div class="brand lh-brand"><span class="brand-square"></span><span class="brand-name">Brookvale<br>Systems</span></div>
    <div class="lh-rule"></div>
    <div class="contact lh-contact">
      <div class="person">Dr. Nora Pellham</div>
      220 Harlow Ridge Road, Ste. 410<br>
      Millbrook, TX 76500<br>
      (800) 555-0148<br><br>
      nora@brookvale-systems.com
    </div>
    <svg class="lh-swoosh" width="90" height="46" viewBox="0 0 90 46">
      <path d="M0,2 L84,0 Q70,10 80,44 Q62,12 0,2 Z" fill="var(--gold)"/>
    </svg>
    <div class="lh-band"><p>THE SYSTEM BUILDERS:&nbsp; Engineering Smarter Business Systems for Every Client</p></div>

    <div class="recipient">
      Dana Whitlock<br>
      Brightframe Creative Services<br>
      dana.brightframe@mail.com<br>
      817-555-0192
    </div>

    <div class="letter">
      <p>Dear Nora,<br>This text will be replaced by your own text. It has been a pleasure working with you. You are a rare and excellent communicator! I would love to talk to you about designing your business cards and web site. Psed diam nonummy nibh euismod tincidunt ut laoreet dolore magna aliquam erat volutpat. Ut wisi enim ad minim veniam, quis nostrud exerci tation ullamcorper suscipit lobortis nisl ut aliquip ex ea commodo consequat. Duis autem vel eum iriure dolor in hendrerit in vulputate velit esse molestie consequat, vel illum dolore eu feugiat nulla facilisis at vero eros et accumsan et iusto odio dignissim qui blandit praesent luptatum zzril delenit augue duis dolore te feugait nulla facilisi.</p>
      <p>Ut wisi enim ad minim veniam, quis nostrud exerci tation ullamcorper suscipit lobortis nisl ut aliquip ex ea commodo consequat. Duis autem vel eum iriure dolor in hendrerit in vulputate velit esse molestie consequat, vel illum dolore eu feugiat nulla facilisis at vero eros et accumsan et iusto odio dignissim qui blandit praesent luptatum zzril delenit augue duis dolore te feugait nulla facilisi. Lorem ipsum dolor sit amet, consectetuer adipiscing elit, sed diam nonummy nibh euismod tincidunt ut laoreet dolore magna aliquam erat volutpat.</p>
      <p>Duis autem vel eum iriure dolor in hendrerit in vulputate velit esse molestie consequat, vel illum dolore eu feugiat nulla facilisis at vero eros et accumsan et iusto odio dignissim qui blandit praesent luptatum zzril delenit augue duis dolore te feugait nulla facilisi. Lorem ipsum dolor sit amet, consectetuer adipiscing elit, sed diam nonummy nibh euismod tincidunt ut laoreet dolore magna aliquam erat volutpat.</p>
    </div>
    <div class="signoff">Sincerely;</div>
    <div class="signature">Dana Whitlock</div>
    <div class="initials">DW/NP</div>

    <svg class="lh-footer" width="504" height="680" viewBox="0 0 504 680">
      <path d="M0,658 C220,640 440,560 504,430" fill="none" stroke="var(--gold)" stroke-width="2"/>
      <path d="M0,664 C225,646 445,566 504,438 L504,680 L0,680 Z" fill="var(--brown)"/>
    </svg>
    <div class="rose-art" role="img" aria-label="Yellow rose illustration"></div>
  </section>

  <section class="envelope env-back">
    <div class="env-flap"></div>
    <div class="env-flap-line"></div>
    <div class="env-flap-brand"><span class="brand-name">Brookvale<br>Systems</span></div>
  </section>

  <section class="envelope env-front">
    <div class="env-stripes">
      <div class="stripe-brown"></div>
      <div class="stripe-gold"></div>
      <div class="stripe-grey"></div>
    </div>
    <div class="brand env-brand"><span class="brand-square"></span><span class="brand-name">Brookvale<br>Systems</span></div>
    <div class="env-rule"></div>
    <div class="contact env-contact">
      <div class="person">Dr. Nora Pellham</div>
      220 Harlow Ridge Road, Ste. 410<br>
      Millbrook, TX 76500<br>
      (800) 555-0148<br><br>
      nora@brookvale-systems.com
    </div>
    <div class="env-tagline"><span>The System Builders</span><span class="divider"></span><em>Engineering Smarter Business Systems for Every Client</em></div>
  </section>

</main>
</body>
</html>
```